Vorla Pty Ltd business card design

We need a business card for our company who is involved in upper market residential property development.
Design should be elegant and contemporary.

Our residences are inspired and elegant in contemporary design, combined with inviting ambience. We produce exclusive boutique developments which appeal to the most discerning of purchasers.
We would like to see a design to reflect the above.

Industry/Entity Type

Residential

Contact Information for Business Card

Vorla Pty Ltd, Marek Dunsworth, PO Box 58 Kelvale 3194 Melbourne AUSTRALIA, ph (+61 3) 0427 5926 84

Logo Text

Vorla Pty Ltd

```html
<!DOCTYPE html>
<html lang="en">
<head>
<meta charset="utf-8">
<title>Vorla Pty Ltd — Business Card</title>
<link rel="stylesheet" href="https://fonts.googleapis.com/css2?family=Arimo:wght@400;700&display=swap">
<style>
  :root {
    --stage: #2a2a2a;
    --card-dark: #2f2f2f;
    --card-light: #ececec;
    --ink-light: #e6e6e6;
    --ink-dark: #1c1c1c;
    --ink-mid: #2b2b2b;
  }
  * { margin: 0; padding: 0; box-sizing: border-box; }
  html, body {
    width: 1200px;
    height: 900px;
    overflow: hidden;
    background: var(--stage);
    font-family: "Arimo", Arial, sans-serif;
  }
  .canvas {
    position: relative;
    width: 1200px;
    height: 900px;
    display: flex;
    align-items: center;
    justify-content: center;
    gap: 60px;
  }
  .card {
    width: 520px;
    height: 297px;
    box-shadow: 0 6px 18px rgba(0,0,0,0.45);
    display: flex;
    flex-direction: column;
    align-items: center;
    justify-content: center;
    text-align: center;
  }
  .card--front { background: var(--card-dark); }
  .card--back { background: var(--card-light); color: var(--ink-dark); }

  .wordmark {
    font-weight: 400;
    letter-spacing: 0.02em;
    white-space: nowrap;
  }
  .card--front .wordmark { color: var(--ink-light); font-size: 54px; }
  .card--back .wordmark { color: var(--ink-dark); font-size: 30px; margin-bottom: 20px; }

  .contact-name {
    font-weight: 700;
    font-size: 19px;
    letter-spacing: 0.03em;
    text-transform: uppercase;
    margin-bottom: 8px;
  }
  .contact-line {
    font-size: 15px;
    line-height: 1.3;
    color: var(--ink-mid);
  }
  .company {
    margin-top: 12px;
    font-size: 15px;
    letter-spacing: 0.04em;
    text-transform: uppercase;
    line-height: 1.15;
  }
  .company-tag {
    font-size: 11px;
    letter-spacing: 0.04em;
    text-transform: uppercase;
    margin-bottom: 6px;
  }
  .address { font-size: 12.5px; color: var(--ink-mid); }
</style>
</head>
<body>
  <main class="canvas">
    <section class="card card--front" aria-label="Card front">
      <p class="wordmark">Vorla Pty Ltd</p>
    </section>

    <section class="card card--back" aria-label="Card back">
      <p class="wordmark">Vorla Pty Ltd</p>
      <p class="contact-name">Marek Dunsworth</p>
      <p class="contact-line">(+61 3) 0427 5926 84</p>
      <p class="contact-line">marek.dun@vorlamail.com</p>
      <p class="company">Vorla Pty Ltd</p>
      <p class="company-tag">Property Group</p>
      <p class="address">PO Box 58 Kelvale 3194 Melbourne AUSTRALIA</p>
    </section>
  </main>
</body>
</html>
```